Talvex Engineering Business card Design

We need to make business cards for our NDT and inspection company. The company is called Talvex Engineering. We want a professional modern feel business card. We have just completed the remaking of our website and would like to have business cards with the same feel and colours. The final design should communicate professionalism and cutting edge tech.

Target Market(s)

We sell to B2B Business clients. Our customer is an engineer or decision maker in the mechanical engineering / Oil and gas field.

Contact Information for Business Card

Please see the current business cards that we have uploaded to get the details. You can also look at our Website www.talvex-eng.example for more.

Requirements
Must have
• Less is more
Nice to have
• Less is more

```html
<!DOCTYPE html>
<html lang="en">
<head>
<meta charset="utf-8">
<title>Talvex Engineering Business Card</title>
<link rel="stylesheet" href="https://fonts.googleapis.com/css2?family=Mulish:wght@400;600;800&family=Libre+Baskerville:wght@700&display=swap">
<style>
  :root {
    --navy: #21315f;
    --red: #a41e25;
    --white: #ffffff;
    --grey-text: #6d6e71;
    --backdrop: #e8e9eb;
  }
  * { box-sizing: border-box; margin: 0; padding: 0; }
  html, body {
    width: 1200px; height: 900px; overflow: hidden;
    background: var(--backdrop);
    font-family: "Mulish", Arial, sans-serif;
  }
  .canvas {
    width: 1200px; height: 900px;
    display: flex; flex-direction: column; align-items: center; justify-content: center;
    gap: 40px;
  }
  .card {
    position: relative;
    width: 700px; height: 400px;
    box-shadow: 0 6px 18px rgba(0,0,0,0.12);
    overflow: hidden;
  }
  /* Back side */
  .card--back { background: var(--navy); color: var(--white); }
  .brand-back {
    position: absolute; top: 62px; left: 0; right: 0;
    display: flex; align-items: center; justify-content: center; gap: 14px;
  }
  .brand-back__dot { width: 34px; height: 34px; border-radius: 50%; background: var(--red); }
  .brand-back__name { font-weight: 800; font-size: 28px; letter-spacing: 0.5px; color: var(--white); }
  .services {
    position: absolute; top: 176px; left: 34px; right: 24px;
    list-style: none;
    font-size: 13.5px; line-height: 34px; letter-spacing: 0.2px;
  }
  .services__row { white-space: nowrap; }
  .services__row:nth-child(2) { padding-left: 10px; }
  .services__row:nth-child(3) { padding-left: 20px; }
  .services__row:nth-child(4) { padding-left: 30px; }
  .services__item::before {
    content: ""; display: inline-block; width: 5px; height: 5px; border-radius: 50%;
    background: var(--red); margin: 0 8px 2px 0; vertical-align: middle;
  }
  .services__item + .services__item { margin-left: 14px; }

  /* Front side */
  .card--front { background: var(--white); }
  .card__band { position: absolute; left: 0; right: 0; bottom: 0; height: 16px; background: var(--navy); }
  .person { position: absolute; top: 70px; left: 60px; }
  .person__accent {
    position: absolute; left: -36px; top: 4px; width: 10px; height: 56px; background: var(--navy);
  }
  .person__name {
    font-family: "Libre Baskerville", Georgia, serif;
    font-weight: 700; font-size: 26px; color: var(--red); letter-spacing: 0.5px;
  }
  .person__title { font-size: 17px; color: var(--grey-text); margin-top: 4px; }
  .address {
    position: absolute; top: 170px; left: 86px;
    font-size: 17px; line-height: 24px; color: var(--grey-text); font-style: normal;
  }
  .contacts {
    position: absolute; top: 262px; left: 66px; list-style: none;
    font-size: 16.5px; line-height: 24px; color: var(--grey-text);
  }
  .contacts li { display: flex; align-items: center; gap: 10px; }
  .contacts svg { width: 14px; height: 14px; fill: var(--navy); flex: none; }
  .brand-front {
    position: absolute; top: 88px; right: 62px;
    display: flex; align-items: center; gap: 14px;
  }
  .brand-front__dot { width: 46px; height: 46px; border-radius: 50%; background: var(--red); }
  .brand-front__name { font-weight: 800; font-size: 40px; color: var(--navy); letter-spacing: 1px; }
  .company-line {
    position: absolute; right: 62px; top: 170px;
    font-weight: 800; font-size: 19px; color: var(--red); letter-spacing: 0.6px;
    white-space: nowrap;
  }
</style>
</head>
<body>
<main class="canvas">
  <section class="card card--back" aria-label="Business card back">
    <div class="brand-back">
      <span class="brand-back__dot"></span>
      <span class="brand-back__name">Talvex Engineering</span>
    </div>
    <ul class="services">
      <li class="services__row"><span class="services__item">API 653 Tank Inspections</span><span class="services__item">API 570 Pipeline Inspections</span><span class="services__item">Welding Inspection</span></li>
      <li class="services__row"><span class="services__item">API 510 Pressure Vessel Inspections</span><span class="services__item">OCTG Inspections</span><span class="services__item">Electrical Inspection</span></li>
      <li class="services__row"><span class="services__item">Non-Destructive Testing</span><span class="services__item">Lifting Equipment Inspections</span><span class="services__item">PAUT / MFL / ILI</span></li>
      <li class="services__row"><span class="services__item">Engineering Projects</span><span class="services__item">UT / PT / MT / RT / VT</span><span class="services__item">Advanced NDT</span></li>
    </ul>
  </section>

  <section class="card card--front" aria-label="Business card front">
    <div class="person">
      <span class="person__accent"></span>
      <h1 class="person__name">DANIEL KERROW</h1>
      <p class="person__title">Managing Director</p>
    </div>
    <address class="address">
      Nyali, Harbour Road<br>
      P.O. BOX 40312-80100<br>
      Kilindini Kenya
    </address>
    <ul class="contacts">
      <li><svg viewBox="0 0 16 16" aria-hidden="true"><path d="M3.6 1.2l2.3 2.6-1.4 1.8c.9 2 2.8 3.9 4.9 4.9l1.8-1.4 2.6 2.3-1.2 2.2C7.4 15.3.7 8.6 1.4 2.4z"/></svg>+ 254 41 555 0142/6</li>
      <li><svg viewBox="0 0 16 16" aria-hidden="true"><path d="M4.5 1h7a1 1 0 0 1 1 1v12a1 1 0 0 1-1 1h-7a1 1 0 0 1-1-1V2a1 1 0 0 1 1-1zm.6 1.6v9.4h5.8V2.6zM8 12.8a.8.8 0 1 0 0 1.6.8.8 0 0 0 0-1.6z"/></svg>+ 254 20 555 0189/3</li>
      <li><svg viewBox="0 0 16 16" aria-hidden="true"><path d="M1 3.5h14v9H1zm1.6 1.4L8 9l5.4-4.1z"/></svg>info@talvex-eng.example</li>
      <li><svg viewBox="0 0 16 16" aria-hidden="true"><path d="M8 1a7 7 0 1 0 0 14A7 7 0 0 0 8 1zm0 1.4c.9.9 1.5 2.4 1.7 4.1H6.3C6.5 4.8 7.1 3.3 8 2.4zM2.5 7.3h2.4c.1 1.7.5 3.2 1.2 4.4a5.6 5.6 0 0 1-3.6-4.4zm0-.8a5.6 5.6 0 0 1 3.6-4.2c-.7 1.2-1.1 2.6-1.2 4.2zm5.5 7.1c-.9-.9-1.5-2.5-1.7-4.3h3.4c-.2 1.8-.8 3.4-1.7 4.3zm1.9-1.9c.7-1.2 1.1-2.7 1.2-4.4h2.4a5.6 5.6 0 0 1-3.6 4.4zm1.2-5.2c-.1-1.6-.5-3-1.2-4.2a5.6 5.6 0 0 1 3.6 4.2z"/></svg>www.talvex-eng.example</li>
    </ul>
    <div class="brand-front">
      <span class="brand-front__dot"></span>
      <span class="brand-front__name">TALVEX</span>
    </div>
    <p class="company-line">TALVEX ENGINEERING FEATURE</p>
    <div class="card__band"></div>
  </section>
</main>
</body>
</html>
```